Business Card Design Project

Business is web based; no retail location. Business card needs to direct potential customers to our website.

Target Market(s)

Parents, Adult Fans of Tumvo

Industry/Entity Type

Retail

Requirements
Must have
• Email Address
Website Address
Should not have
• Telephone Number

```html
<!DOCTYPE html>
<html lang="en">
<head>
<meta charset="utf-8">
<title>Harbor Town Blocks – Business Card</title>
<link rel="stylesheet" href="https://fonts.googleapis.com/css2?family=Tinos:wght@400;700&display=swap">
<style>
  :root {
    --page-bg: #ffffff;
    --card-maroon-deep: #2e1114;
    --card-maroon: #4a1a1e;
    --card-glow: #9a2226;
    --rim-black: #0c0c0c;
    --panel-white: #ffffff;
    --brick-yellow: #f2b705;
    --brick-orange: #e3560f;
    --brick-red: #d8141b;
    --wordmark-red: #8d1a20;
    --contact-ink: #f3e8e8;
  }
  html, body {
    margin: 0;
    padding: 0;
    width: 1200px;
    height: 900px;
    overflow: hidden;
    background: var(--page-bg);
  }
  .canvas {
    position: relative;
    width: 1200px;
    height: 900px;
  }
  .business-card {
    position: absolute;
    left: 164px;
    top: 211px;
    width: 864px;
    height: 494px;
    border-radius: 22px;
    overflow: hidden;
    box-shadow: 0 2px 10px rgba(0, 0, 0, 0.18);
  }
  .card-shapes {
    position: absolute;
    inset: 0;
    width: 864px;
    height: 494px;
    display: block;
  }
  .brick-illustration {
    position: absolute;
    left: 156px;
    top: 44px;
    width: 268px;
    height: 392px;
    border-radius: 10px;
    background: linear-gradient(172deg,
      var(--brick-yellow) 0%,
      var(--brick-yellow) 38%,
      var(--brick-orange) 47%,
      var(--brick-red) 56%,
      var(--brick-red) 100%);
  }
  .wordmark {
    position: absolute;
    left: 452px;
    top: 108px;
    height: 280px;
    margin: 0;
    writing-mode: vertical-rl;
    transform: rotate(180deg);
    font-family: "Tinos", serif;
    font-weight: 700;
    font-size: 44px;
    line-height: 50px;
    color: var(--wordmark-red);
    text-align: center;
  }
  .wordmark span { display: block; }
  .contact {
    position: absolute;
    left: 741px;
    top: 60px;
    height: 370px;
    margin: 0;
    writing-mode: vertical-rl;
    transform: rotate(180deg);
    font-family: "Tinos", serif;
    font-weight: 400;
    font-size: 17px;
    line-height: 33px;
    letter-spacing: 1.5px;
    color: var(--contact-ink);
    text-align: center;
    white-space: nowrap;
  }
  .contact span { display: block; }
</style>
</head>
<body>
<main class="canvas">
  <section class="business-card" aria-label="Harbor Town Blocks business card">
    <svg class="card-shapes" viewBox="0 0 594 340" preserveAspectRatio="none" aria-hidden="true">
      <defs>
        <radialGradient id="side-glow" cx="594" cy="165" r="150" gradientUnits="userSpaceOnUse" gradientTransform="translate(594 165) scale(0.6 1.2) translate(-594 -165)">
          <stop offset="0" stop-color="var(--card-glow)"/>
          <stop offset="1" stop-color="var(--card-maroon-deep)"/>
        </radialGradient>
        <linearGradient id="left-band" x1="0" y1="0" x2="1" y2="0">
          <stop offset="0" stop-color="var(--card-maroon-deep)"/>
          <stop offset="1" stop-color="var(--card-maroon)"/>
        </linearGradient>
      </defs>
      <rect class="card-base" x="0" y="0" width="594" height="340" fill="url(#side-glow)"/>
      <rect class="card-left-band" x="0" y="0" width="90" height="340" fill="url(#left-band)"/>
      <path class="panel-rim" d="M66,0 Q2,170 66,340 L450,340 Q510,170 450,0 Z" fill="var(--rim-black)"/>
      <path class="panel-white" d="M72,0 Q12,170 72,340 L442,340 Q498,170 442,0 Z" fill="var(--panel-white)"/>
    </svg>

    <div class="brick-illustration" role="img" aria-label="Illustration of two stacked toy building bricks, a yellow brick above a red brick"></div>

    <h1 class="wordmark"><span>Harbor</span><span>Town</span><span>Blocks</span></h1>

    <p class="contact">
      <span class="contact-email">XXXXXXXXXXXXX@MAILBOX.COM</span>
      <span class="contact-web">WWW.XXXXXXXXXXXXXXX.COM</span>
    </p>
  </section>
</main>
</body>
</html>
```